Lip Balm Label Design

Design a label for a Lavender-Mint lip balm. We make high-quality natural essential oil products. Please use the old label as an example of what exists. The label should include purple. The final design should be eye-catching and distinct. The file should be in an AI file.

Here is the information that should be included on the label:
1) ingredients:Theobroma Cacao (Cocoa) Seed Butter, Theobroma grandiflorum Ultra Refined Butter, beesewax, Calendula Officinalis Flower Oil, Prunus Amygdalus Dulcis (Sweet Almond) Oil, cetyl alcohol and Tocopherol. Lavandula Angustifolia (Lavender) Oil and Mentha Piperita (Peppermint) Oil.

2) www.kelvorascents.com

3) Brand name and logo: K. Velora Aromatherapy (logo is attached- you can use with form)

```html
<!DOCTYPE html>
<html lang="en">
<head>
<meta charset="utf-8">
<title>Lavender-Mint Lip Balm Label</title>
<link rel="stylesheet" href="https://fonts.googleapis.com/css2?family=Cinzel:wght@400;500&family=Montserrat:wght@500;700;800&family=Open+Sans:wght@400;600&display=swap">
<style>
  :root {
    --label-bg: #ddd4e9;
    --band: #6a2a86;
    --deep-purple: #5c2a82;
    --plum: #8c2384;
    --mint: #2f9a48;
    --text-dark: #1f1a24;
    --badge-ring: #6a2a86;
    --leaf-grey: rgba(170, 162, 180, 0.55);
  }
  * { margin: 0; padding: 0; box-sizing: border-box; }
  html, body { width: 1200px; height: 954px; overflow: hidden; background: var(--label-bg); }
  .label {
    position: relative;
    width: 1200px;
    height: 954px;
    background: var(--label-bg);
    overflow: hidden;
  }
  .band { position: absolute; left: 0; width: 1200px; background: var(--band); }
  .band--top { top: 0; height: 15px; }
  .band--bottom { bottom: 0; height: 32px; }

  .leaf-backdrop {
    position: absolute;
    left: 250px; top: 140px;
    width: 720px; height: 760px;
    border-radius: 50% 50% 46% 46%;
    background: radial-gradient(ellipse at 50% 55%, var(--leaf-grey) 0%, rgba(190,182,200,0.35) 45%, rgba(221,212,233,0) 72%);
  }

  .brand {
    position: absolute;
    left: 400px; top: 68px;
    width: 400px;
    text-align: center;
    font-family: "Cinzel", serif;
    font-weight: 500;
    color: var(--plum);
    font-size: 52px;
    line-height: 1;
  }
  .brand small { display: block; font-size: 19px; letter-spacing: 0.5px; margin-top: 6px; padding-left: 120px; }

  .product-name {
    position: absolute;
    left: 335px; top: 258px;
    width: 480px;
    text-align: center;
    font-family: "Cinzel", serif;
    font-weight: 500;
    line-height: 1;
  }
  .product-name .flavour-a { display: block; color: var(--plum); font-size: 62px; }
  .product-name .flavour-b { display: block; color: var(--mint); font-size: 62px; margin-top: 10px; }
  .product-name .product-type { display: block; color: var(--plum); font-size: 46px; margin-top: 20px; }

  .flower-art {
    position: absolute;
    left: 390px; top: 495px;
    width: 500px; height: 330px;
    border-radius: 50% 50% 48% 48% / 60% 60% 40% 40%;
    background: linear-gradient(160deg, #a3268f 0%, #7a2c8c 55%, #5d2a82 100%);
  }

  .handmade-badge {
    position: absolute;
    left: 728px; top: 456px;
    width: 180px; height: 180px;
  }

  .net-weight {
    position: absolute;
    left: 390px; top: 852px;
    width: 410px;
    text-align: center;
    font-family: "Cinzel", serif;
    font-size: 38px;
    color: var(--deep-purple);
  }

  .claims {
    position: absolute;
    left: 154px; top: 51px;
    width: 132px;
    display: flex;
    flex-direction: column;
    gap: 33px;
  }
  .claim-badge { width: 132px; height: 132px; display: block; }
  .claim-badge text { font-family: "Montserrat", sans-serif; font-weight: 800; font-size: 10.5px; fill: var(--badge-ring); letter-spacing: 0.3px; }

  .website {
    position: absolute;
    left: 20px; top: 890px;
    width: 500px; height: 48px;
    transform-origin: top left;
    transform: rotate(-90deg);
    text-align: center;
    font-family: "Montserrat", sans-serif;
    font-weight: 500;
    font-size: 35px;
    color: var(--deep-purple);
    white-space: nowrap;
  }

  .ingredients {
    position: absolute;
    left: 953px; top: 902px;
    width: 890px; height: 234px;
    transform-origin: top left;
    transform: rotate(-90deg);
    font-family: "Open Sans", sans-serif;
    font-size: 25px;
    line-height: 39px;
    letter-spacing: -0.2px;
    color: var(--text-dark);
    white-space: nowrap;
  }
  .ingredients strong { font-weight: 600; }
</style>
</head>
<body>
<main class="label">
  <div class="band band--top"></div>

  <div class="leaf-backdrop" role="img" aria-label="Large faint grey leaf shapes in the background"></div>

  <div class="brand">K. Velora<small>Aromatherapy</small></div>

  <div class="claims">
    <svg class="claim-badge" viewBox="0 0 132 132" role="img" aria-label="Organic cosmetics">
      <defs>
        <path id="arc-top" d="M 19 66 A 47 47 0 0 1 113 66"/>
        <path id="arc-bottom" d="M 12 66 A 54 54 0 0 0 120 66"/>
      </defs>
      <circle cx="66" cy="66" r="62" fill="none" stroke="var(--badge-ring)" stroke-width="5"/>
      <circle cx="66" cy="66" r="40" fill="none" stroke="var(--badge-ring)" stroke-width="4"/>
      <circle cx="66" cy="66" r="24" fill="var(--badge-ring)" opacity="0.85" role="img" aria-label="Leaf icon"/>
      <text><textPath href="#arc-top" startOffset="50%" text-anchor="middle">ORGANIC</textPath></text>
      <text><textPath href="#arc-bottom" startOffset="50%" text-anchor="middle">COSMETICS</textPath></text>
    </svg>
    <svg class="claim-badge" viewBox="0 0 132 132" role="img" aria-label="Paraben free">
      <circle cx="66" cy="66" r="62" fill="none" stroke="var(--badge-ring)" stroke-width="5"/>
      <circle cx="66" cy="66" r="40" fill="none" stroke="var(--badge-ring)" stroke-width="4"/>
      <circle cx="66" cy="66" r="24" fill="var(--badge-ring)" opacity="0.85" role="img" aria-label="Molecule icon crossed out"/>
      <text><textPath href="#arc-top" startOffset="50%" text-anchor="middle">PARABEN FREE</textPath></text>
      <text><textPath href="#arc-bottom" startOffset="50%" text-anchor="middle">PARABEN FREE</textPath></text>
    </svg>
    <svg class="claim-badge" viewBox="0 0 132 132" role="img" aria-label="Sulfates free">
      <circle cx="66" cy="66" r="62" fill="none" stroke="var(--badge-ring)" stroke-width="5"/>
      <circle cx="66" cy="66" r="40" fill="none" stroke="var(--badge-ring)" stroke-width="4"/>
      <circle cx="66" cy="66" r="24" fill="var(--badge-ring)" opacity="0.85" role="img" aria-label="Atom icon"/>
      <text><textPath href="#arc-top" startOffset="50%" text-anchor="middle">SULFATES FREE</textPath></text>
      <text><textPath href="#arc-bottom" startOffset="50%" text-anchor="middle">SULFATES FREE</textPath></text>
    </svg>
    <svg class="claim-badge" viewBox="0 0 132 132" role="img" aria-label="Not tested on animals">
      <circle cx="66" cy="66" r="62" fill="none" stroke="var(--badge-ring)" stroke-width="5"/>
      <circle cx="66" cy="66" r="40" fill="none" stroke="var(--badge-ring)" stroke-width="4"/>
      <circle cx="66" cy="66" r="24" fill="var(--badge-ring)" opacity="0.85" role="img" aria-label="Paw print icon crossed out"/>
      <text><textPath href="#arc-top" startOffset="50%" text-anchor="middle">NOT TESTED</textPath></text>
      <text><textPath href="#arc-bottom" startOffset="50%" text-anchor="middle">ON ANIMALS</textPath></text>
    </svg>
    <svg class="claim-badge" viewBox="0 0 132 132" role="img" aria-label="Natural cosmetics">
      <circle cx="66" cy="66" r="62" fill="none" stroke="var(--badge-ring)" stroke-width="5"/>
      <circle cx="66" cy="66" r="40" fill="none" stroke="var(--badge-ring)" stroke-width="4"/>
      <circle cx="66" cy="66" r="24" fill="var(--badge-ring)" opacity="0.85" role="img" aria-label="Leaf icon"/>
      <text><textPath href="#arc-top" startOffset="50%" text-anchor="middle">NATURAL</textPath></text>
      <text><textPath href="#arc-bottom" startOffset="50%" text-anchor="middle">COSMETICS</textPath></text>
    </svg>
  </div>

  <div class="website">www.kelvorascents.com</div>

  <h1 class="product-name">
    <span class="flavour-a">Lavender-</span>
    <span class="flavour-b">Mint</span>
    <span class="product-type">Lip Balm</span>
  </h1>

  <div class="flower-art" role="img" aria-label="Purple lotus flower illustration"></div>

  <svg class="handmade-badge" viewBox="0 0 196 196" role="img" aria-label="100% handmade, made with love seal">
    <defs>
      <path id="seal-arc-top" d="M 32 98 A 66 66 0 0 1 164 98"/>
      <path id="seal-arc-bottom" d="M 24 98 A 74 74 0 0 0 172 98"/>
    </defs>
    <circle cx="98" cy="98" r="94" fill="var(--deep-purple)"/>
    <circle cx="98" cy="98" r="86" fill="none" stroke="#ffffff" stroke-width="2"/>
    <circle cx="98" cy="98" r="46" fill="#b79ac9" role="img" aria-label="Hand with heart icon"/>
    <text font-family="Montserrat, sans-serif" font-weight="700" font-size="17" fill="#ffffff" letter-spacing="1">
      <textPath href="#seal-arc-top" startOffset="50%" text-anchor="middle">100% HANDMADE</textPath>
    </text>
    <text font-family="Montserrat, sans-serif" font-weight="700" font-size="17" fill="#ffffff" letter-spacing="1">
      <textPath href="#seal-arc-bottom" startOffset="50%" text-anchor="middle">MADE WITH LOVE</textPath>
    </text>
  </svg>

  <div class="net-weight">15 OZ (4.4ML)</div>

  <p class="ingredients"><strong>Ingredients:</strong>Theobroma Cacao (Cocoa) Seed Butter,<br>Theobroma grandiflorum Ultra Refined Butter, beesewax,<br>Calendula Officinalis Flower Oil, Prunus Amygdalus Dulcis<br>(Sweet Almond) Oil, cetyl alcohol and Tocopherol.<br>Lavandula Angustifolia (Lavender) Oil and Mentha Piperita<br>(Peppermint) Oil.</p>

  <div class="band band--bottom"></div>
</main>
</body>
</html>
```